Kelvane Plumbing Business cards

Company is Kelvane Plumbing.
name Dashel Morrowby, I am a plumber, drainer, gasfitter and roofer
Mobile: 0431 906 154
Email address: info@kelvaneplumbing.example (check out my website for some ideas)
Website: www.kelvaneplumbing.example
ABN: 82 916 203 471
LIC: 604517K

I am reliable all round plumber. I am a 24 hour emergency service. Kelvane Plumbing is a professional plumbing service in the Illawarra, South Coast, Southern Sydney and Southern Highland regions of NSW. We offer a 24 hour emergency service for piece of mind to our customers. Call us now to see how we can help you. Kelvane Plumbing approaches every job with attention to detail and excellent customer service. With our superior workmanship you can be confident that the job will be done right the first time around. You can rest assured with results that are guaranteed to last.

Target Market(s)

the general public

Contact Information for Business Card

look up website for some ideas something with similar colours to logo and new modern and to catch the eye.

Colors
fdfdfd
ffffff
000000
7f7f7f
aaaaaa
33a6d7
0492cd

Requirements
Must have
• all contact details
• company- Kelvane Plumbing
• name- Dashel Morrowby
• number mobile- 0431 906 154
• Email address- info@kelvaneplumbing.example
• Website- www.kelvaneplumbing.example
• ABN- 82 916 203 471
• LIC- 604517K

```html
<!DOCTYPE html>
<html lang="en">
<head>
<meta charset="utf-8">
<title>Kelvane Plumbing Business Cards</title>
<link href="https://fonts.googleapis.com/css2?family=Roboto:wght@400;500&family=Roboto+Condensed:wght@400&display=swap" rel="stylesheet">
<style>
  :root {
    --backdrop: #e4e4e4;
    --card: #000000;
    --white: #ffffff;
    --grey: #7f7f7f;
    --blue: #0492cd;
    --blue-light: #33a6d7;
  }
  html, body {
    margin: 0;
    padding: 0;
    width: 1125px;
    height: 1200px;
    overflow: hidden;
    background: var(--backdrop);
  }
  .sheet {
    position: relative;
    width: 1125px;
    height: 1200px;
  }
  .card {
    position: absolute;
    left: 171px;
    width: 826px;
    height: 472px;
    background: var(--card);
    color: var(--white);
    font-family: "Roboto", Arial, sans-serif;
    overflow: hidden;
  }
  .card-front { top: 106px; }
  .card-back { top: 639px; }

  .brand-front {
    position: absolute;
    right: 60px;
    top: 108px;
    margin: 0;
    font-family: "Roboto", Arial, sans-serif;
    font-weight: 500;
    font-size: 34px;
    letter-spacing: 0.04em;
    text-transform: uppercase;
    color: var(--blue);
  }

  .holder-name {
    position: absolute;
    left: 55px;
    top: 286px;
    margin: 0;
    font-family: "Roboto Condensed", Arial, sans-serif;
    font-weight: 400;
    font-size: 31px;
    color: var(--blue);
    text-transform: uppercase;
  }
  .divider {
    position: absolute;
    left: 64px;
    top: 345px;
    width: 704px;
    height: 1px;
    background: var(--white);
  }
  .contact-list {
    position: absolute;
    left: 55px;
    top: 364px;
    margin: 0;
    padding: 0;
    list-style: none;
    font-size: 20px;
    line-height: 27px;
  }
  .contact-list li {
    display: flex;
    align-items: center;
    gap: 10px;
  }
  .contact-list svg { width: 19px; height: 19px; fill: var(--blue); }
  .registration {
    position: absolute;
    right: 60px;
    top: 370px;
    margin: 0;
    text-align: right;
    font-size: 20px;
    line-height: 25px;
  }
  .front-bands {
    position: absolute;
    left: 0;
    top: 436px;
    width: 826px;
    height: 36px;
  }
  .front-web {
    position: absolute;
    right: 60px;
    top: 441px;
    font-size: 20px;
    color: var(--white);
  }

  .brand-back {
    position: absolute;
    left: 0;
    right: 0;
    top: 205px;
    display: flex;
    justify-content: center;
    align-items: center;
    gap: 14px;
    margin: 0;
    font-weight: 500;
    font-size: 38px;
    letter-spacing: 0.04em;
    text-transform: uppercase;
    color: var(--blue);
  }
  .brand-dot {
    width: 18px;
    height: 18px;
    border-radius: 50%;
    background: var(--blue);
  }
  .back-web {
    position: absolute;
    left: 0;
    right: 0;
    top: 410px;
    text-align: center;
    font-size: 20px;
    letter-spacing: 0.45em;
    color: var(--white);
  }
</style>
</head>
<body>
<main class="sheet">
  <section class="card card-front" aria-label="Business card front">
    <p class="brand-front">Kelvane Plumbing</p>
    <h1 class="holder-name">Dashel Morrowby</h1>
    <div class="divider"></div>
    <ul class="contact-list">
      <li>
        <svg viewBox="0 0 24 24" aria-hidden="true"><path d="M6.6 10.8a15.1 15.1 0 0 0 6.6 6.6l2.2-2.2a1 1 0 0 1 1-.25 11.4 11.4 0 0 0 3.6.57 1 1 0 0 1 1 1V20a1 1 0 0 1-1 1A17 17 0 0 1 3 4a1 1 0 0 1 1-1h3.5a1 1 0 0 1 1 1c0 1.25.2 2.45.57 3.57a1 1 0 0 1-.25 1z"/></svg>
        <span>0431 906 154</span>
      </li>
      <li>
        <svg viewBox="0 0 24 24" aria-hidden="true"><path d="M2 5h20v14H2z M3.5 6.5 12 13l8.5-6.5" fill="var(--blue)" stroke="#000" stroke-width="1.5"/></svg>
        <span>info@kelvaneplumbing.example</span>
      </li>
    </ul>
    <p class="registration">ABN- 82 916 203 471<br>LIC- 604517K</p>
    <svg class="front-bands" viewBox="0 0 826 36" aria-hidden="true">
      <polygon points="0,21 480,21 466,36 0,36" fill="var(--grey)"/>
      <polygon points="504,0 826,0 826,36 466,36" fill="var(--blue)"/>
    </svg>
    <span class="front-web">www.kelvaneplumbing.example</span>
  </section>

  <section class="card card-back" aria-label="Business card back">
    <p class="brand-back"><span class="brand-dot"></span>Kelvane Plumbing</p>
    <p class="back-web">www.kelvaneplumbing.example</p>
  </section>
</main>
</body>
</html>
```